Website Design for Dealership
Need Website Designer- examples provided
I have given feedback- please submit any requested changes, we are looking to choose our winner by tomorrow afternoon.
Why did the contest get extended? Any feedback on the designs?
RT/KWF/NJ Team
Dear QD,
Kindly upload Logos and photos as mentioned by you so that we can start working on this project.
thanks
quillforge
I have 2 Adobe Illustrator files of the logos we are to use on the website. The red oval one is the Manufacturer. The ‘Haulwright of NYC’ is our specific location. I also have 8 .jpegs of trucks you can use on the site.
Lastly-
We really want the website to model the Atlanta Haulwright website example we provided. The only differences are- we do not have a body shop. The tabs/categories that should be displayed on the website are:
“Home/Truck Sales/Service/Parts/About Us”

```html
<!DOCTYPE html>
<html lang="en">
<head>
<meta charset="utf-8">
<title>Haulwright of New York City</title>
<link href="https://fonts.googleapis.com/css2?family=Arimo:wght@400;700&family=Open+Sans:wght@400;600;700&display=swap" rel="stylesheet">
<style>
  :root {
    --red-deep: #7a0006;
    --red-mid: #b8000c;
    --red-bright: #d8121a;
    --blue-dark: #0b3a66;
    --blue-mid: #1a5d98;
    --blue-light: #2f86c8;
    --white: #ffffff;
    --panel-grey: #efefef;
    --divider: #d8d8d8;
    --text-dark: #4a4a4a;
    --text-grey: #9a9a9a;
    --heading-red: #cc0a0a;
  }
  * { margin: 0; padding: 0; box-sizing: border-box; }
  html, body { width: 1200px; height: 961px; overflow: hidden; }
  body {
    position: relative;
    font-family: "Open Sans", sans-serif;
    background: radial-gradient(ellipse at 50% 45%, var(--red-bright) 0%, var(--red-mid) 55%, var(--red-deep) 100%);
  }
  .brand {
    position: absolute; left: 92px; top: 34px;
    display: flex; align-items: center; gap: 14px;
  }
  .brand-mark { width: 44px; height: 44px; background: var(--white); }
  .brand-name {
    font-family: "Arimo", sans-serif; font-weight: 700; font-size: 30px;
    color: var(--white); line-height: 1.05;
  }
  .page {
    position: absolute; left: 78px; top: 118px; width: 1044px; height: 778px;
    background: var(--white);
    box-shadow: 0 0 22px rgba(0,0,0,0.45);
  }
  .page::before {
    content: ""; position: absolute; left: 0; top: 0; width: 100%; height: 8px;
    background: linear-gradient(var(--blue-light), var(--blue-dark));
  }
  .main-nav {
    position: absolute; left: 28px; top: 66px; width: 164px; height: 237px;
    background: linear-gradient(180deg, var(--blue-mid), var(--blue-dark));
    border-radius: 4px; box-shadow: 0 3px 8px rgba(0,0,0,0.35);
    list-style: none; padding-top: 4px;
  }
  .main-nav li {
    height: 45px; line-height: 45px; padding-left: 16px;
    color: var(--white); font-size: 18px; letter-spacing: 0.3px;
    border-bottom: 1px solid rgba(255,255,255,0.15);
  }
  .main-nav li:last-child { border-bottom: none; }
  .main-nav li.active { background: rgba(0,20,50,0.45); }
  .intro-title {
    position: absolute; left: 226px; top: 60px;
    font-family: "Arimo", sans-serif; font-weight: 700; font-size: 34px;
    color: var(--heading-red);
  }
  .intro-text {
    position: absolute; left: 226px; top: 114px; width: 388px;
    font-size: 17px; line-height: 23px; color: var(--text-dark);
    text-align: justify;
  }
  .learn-more {
    position: absolute; left: 439px; top: 275px; width: 150px; height: 52px;
    border-radius: 6px;
    background: linear-gradient(180deg, var(--blue-light), var(--blue-mid) 55%, var(--blue-dark));
    box-shadow: 0 3px 6px rgba(0,0,0,0.3);
    color: var(--white); font-size: 14px; font-weight: 700;
    display: flex; align-items: center; padding-left: 12px; gap: 10px;
  }
  .learn-more svg { width: 22px; height: 22px; }
  .showcase {
    position: absolute; left: 628px; top: 38px; width: 370px; height: 280px;
    background: linear-gradient(180deg, #b9b9b9, #8d8d8d);
    border-radius: 4px; padding: 10px;
    box-shadow: 0 6px 12px rgba(0,0,0,0.3);
  }
  .showcase-photo {
    width: 100%; height: 100%;
    background: linear-gradient(180deg, #8fb2d8 0%, #c8d6e4 40%, #6f8a55 62%, #5e5e5e 100%);
  }
  .slide-arrow {
    position: absolute; top: 148px; width: 30px; height: 30px;
  }
  .slide-arrow.prev { left: 616px; }
  .slide-arrow.next { left: 972px; }
  .features {
    position: absolute; left: 0; top: 362px; width: 1044px; height: 333px;
    background: linear-gradient(180deg, #f6f6f6, var(--panel-grey));
    display: flex;
  }
  .feature {
    flex: 1; position: relative; text-align: center;
    border-right: 1px solid var(--divider);
  }
  .feature:last-child { border-right: none; }
  .feature-photo {
    margin: 38px auto 0; width: 156px; height: 120px;
    border: 3px solid var(--white); box-shadow: 0 2px 6px rgba(0,0,0,0.3);
  }
  .feature-photo.one { background: linear-gradient(180deg, #9cc0dc, #e8e8e8 55%, #7a7a7a); }
  .feature-photo.two { background: linear-gradient(180deg, #c7a57f, #b23a2a 55%, #6b5a48); }
  .feature-photo.three { background: linear-gradient(180deg, #dfd0a8, #b7282a 55%, #8a7a5e); }
  .feature p {
    width: 190px; margin: 16px auto 0;
    font-size: 13px; line-height: 19px; color: var(--text-grey);
    text-transform: uppercase; text-align: justify;
  }
  .site-footer {
    position: absolute; left: 0; top: 695px; width: 1044px; height: 83px;
    background: linear-gradient(180deg, var(--blue-light), var(--blue-mid) 45%, var(--blue-dark));
    color: var(--white); text-align: center;
  }
  .footer-links { padding-top: 14px; font-size: 19px; letter-spacing: 0.3px; }
  .copyright { font-size: 16px; margin-top: 2px; }
</style>
</head>
<body>
  <header class="brand">
    <span class="brand-mark"></span>
    <span class="brand-name">Haulwright of<br>New York City</span>
  </header>

  <main class="page">
    <ul class="main-nav">
      <li class="active">HOME</li>
      <li>TRUCK SALES</li>
      <li>SERVICE</li>
      <li>PARTS</li>
      <li>ABOUT US</li>
    </ul>

    <h1 class="intro-title">LOREM IPSUM</h1>
    <p class="intro-text">Lorem ipsum dolor sit amet, consectetur adipisicing elit, sed do eiusmod tempor incididunt ut labore et dolore magna aliqua. Ut enim ad minim veniam.</p>

    <div class="learn-more">LEARN MORE
      <svg viewBox="0 0 22 22"><circle cx="11" cy="11" r="10" fill="#ffffff"/><path d="M8 5 L14 11 L8 17" fill="none" stroke="#1a5d98" stroke-width="3"/></svg>
    </div>

    <div class="showcase">
      <div class="showcase-photo" role="img" aria-label="Green and white box truck driving on a mountain road"></div>
    </div>
    <svg class="slide-arrow prev" viewBox="0 0 30 30"><rect width="30" height="30" rx="3" fill="#cc0a0a"/><path d="M19 8 L10 15 L19 22 Z" fill="#ffffff"/></svg>
    <svg class="slide-arrow next" viewBox="0 0 30 30"><rect width="30" height="30" rx="3" fill="#cc0a0a"/><path d="M11 8 L20 15 L11 22 Z" fill="#ffffff"/></svg>

    <section class="features">
      <div class="feature">
        <div class="feature-photo one" role="img" aria-label="White box truck parked on a lot"></div>
        <p>Lorem ipsum dolor sit amet, consectetur adipiscing elit, sed do eiusmod tempor incididunt ut labore et dolore magna aliqua. Ut enim ad minim veniam.</p>
      </div>
      <div class="feature">
        <div class="feature-photo two" role="img" aria-label="Red truck parked outside a service building"></div>
        <p>Lorem ipsum dolor sit amet, consectetur adipiscing elit, sed do eiusmod tempor incididunt ut labore et dolore magna aliqua. Ut enim ad minim veniam.</p>
      </div>
      <div class="feature">
        <div class="feature-photo three" role="img" aria-label="Red dump truck on a work site"></div>
        <p>Lorem ipsum dolor sit amet, consectetur adipiscing elit, sed do eiusmod tempor incididunt ut labore et dolore magna aliqua. Ut enim ad minim veniam.</p>
      </div>
    </section>

    <footer class="site-footer">
      <div class="footer-links">HOME | TRUCK SALES | SERVICE | PARTS | ABOUT US</div>
      <div class="copyright">COPYRIGHT @ 2012 www.haulwrightatl.com</div>
    </footer>
  </main>
</body>
</html>
```